Velmora CBD Tincture packaging design

We are seeking a designer to create the label that will be printed on cardboard box packaging, which will carry our CBD tincture. We envision the box being white to resemble a clean look that stands out on shelves. Our logo (attached) uses shades of yellows and greens in the form of a fluid drop resembling half plant and half plant extract. The packaging will show that we only use clean (TRUNK certified) hemp extract thats been extracted using the cleanest method of extraction; supercritical CO2. Our tincture uses a fractionated coconut oil to improve absorption for the consumer, increasing onset time and providing essential omega fatty acids. We take pride in our use of a clean product with a clean extraction. The tincture bottle itself holds 30ml of liquid and is a clear glass bottle. The cap for the tincture bottle is white and has a graduated glass stem that shows the measurements for how much liquid it holds (picture attached). We have not yet done the label that will stick on the tincture, but i image it will be a frosted white label with the Velmora logo and a few words describing the product. This project is for the cardboard box that will hold each individual tincture bottle.

BOX DIMENSIONS: 1.31" x 1.31" x 4.13" (LxWxH)

We will be releasing a new product (cbd capsules) in April, and we will reach out to the designer of this product as first option to create the design for the capsule packaging.

Target Market(s)

convenience stores, medical marijuana dispensaries, health stores

Font styles to use
Serif

Colors
ffffff
fbed22
ffc214
ffcf3e
acd136
9bcb3c

Requirements
Must have
• -Velmora company logo
-Made with full spectrum supercritical CO2 Hemp Extract
-Made from TRUNK certified clean hemp
-Declaration of ingredients (fractionated coconut oil, CBD hemp extract)
-1200mg CBD Tincture
-Nt. Wt. 1FL OZ (30ml)
-These statements have not been evaluated by the Food and Drug Administration. FDA has not evaluated this product for safety or efficacy. This product is not intended to diagnose, treat, cure or prevent any disease.
-DO NOT REFRIGERATE. Keep at room temperature to preserve freshness. Store away from humidity, heat, and light. Warning: If pregnant, nursing or taking prescription drugs, consult your physician prior to use. Keep out of reach of children.
-Manufactured by Velmora CBD Co. 58 Quarry Bend Rd. Scarborough, ME 04019
-Batch ID:___________
-Expiration Date:____________
-Good Manufacturing Practice (GMP) Logo
-TRUNK logo
Nice to have
• -Contains omega 3, 6 and essential fatty acids
-Graduated dropper for precise dosing
-40mg of CBD per dropper!
-Made in the USA
-No Pesticides
-No Solvents
-No Heavy Metals
-CO2 Extraction
-3rd Party Lab Tested

```html
<!DOCTYPE html>
<html lang="en">
<head>
<meta charset="utf-8">
<title>Velmora CBD Tincture – Box Panels</title>
<link href="https://fonts.googleapis.com/css2?family=League+Spartan:wght@500;700;800&family=Oswald:wght@300;400;500&display=swap" rel="stylesheet">
<style>
  :root{
    --stage:#d9dbde;
    --white:#ffffff;
    --ink:#262626;
    --green-deep:#2f8f25;
    --green-mid:#4aa82d;
    --green-light:#6dbb35;
    --amber:#d78b2b;
    --mist:#f1f1f1;
  }
  *{margin:0;padding:0;box-sizing:border-box}
  html,body{width:1200px;height:1200px;overflow:hidden;background:var(--stage)}
  .stage{position:relative;width:1200px;height:1200px;display:flex;justify-content:center;align-items:center}
  .box{display:flex;height:1120px;box-shadow:0 10px 30px rgba(0,0,0,.12)}
  .panel{position:relative;height:100%;background:var(--white);overflow:hidden;display:flex;flex-direction:column}
  .panel--side{width:380px;border-right:1px solid #e2e2e2}
  .panel--front{width:560px}

  .brand{height:270px;flex:none;display:flex;align-items:flex-end;justify-content:center;padding-bottom:50px;gap:12px}
  .brand__name{font-family:"League Spartan",sans-serif;font-weight:500;color:var(--ink);letter-spacing:-1px;line-height:1}
  .panel--front .brand__name{font-size:86px}
  .panel--side .brand__name{font-size:62px}
  .brand__dot{border-radius:50%;background:var(--amber)}
  .panel--front .brand__dot{width:22px;height:22px;margin-bottom:14px}
  .panel--side .brand__dot{width:16px;height:16px;margin-bottom:10px}

  .band-green{height:290px;flex:none;background:linear-gradient(90deg,var(--green-deep),var(--green-mid) 55%,var(--green-light));color:var(--white);text-align:center}
  .band-amber{height:50px;flex:none;background:var(--amber);color:var(--white);display:flex;align-items:center;justify-content:center;font-family:"Oswald",sans-serif;font-weight:500}

  .front-spectrum{font-family:"Oswald",sans-serif;font-weight:400;font-size:24px;padding-top:34px;letter-spacing:.2px;line-height:1.2}
  .front-title{font-family:"League Spartan",sans-serif;font-weight:800;font-size:90px;line-height:.95;margin-top:22px;text-shadow:2px 3px 0 rgba(0,60,0,.25)}
  .band-amber--front{font-size:23px}

  .lower{position:relative;flex:1;text-align:center}
  .lower__wash{position:absolute;inset:0;background:linear-gradient(180deg,var(--white),var(--mist))}
  .lower__content{position:relative}

  .front-mark{width:46px;height:46px;border-radius:50%;background:var(--amber);margin:44px auto 0}
  .front-mg{font-family:"League Spartan",sans-serif;font-weight:700;font-size:66px;color:var(--ink);margin-top:30px;line-height:1}
  .front-cbd{font-family:"League Spartan",sans-serif;font-weight:800;font-size:128px;color:var(--amber);line-height:.9;margin-top:10px}
  .front-tincture{font-family:"League Spartan",sans-serif;font-weight:700;font-size:54px;color:var(--ink);line-height:1;margin-top:8px}
  .front-net{font-family:"League Spartan",sans-serif;font-weight:500;font-size:20px;color:#444;margin-top:56px}

  .side-green{padding:30px 22px 0}
  .side-heading{font-family:"Oswald",sans-serif;font-weight:500;font-size:17px;text-transform:uppercase;line-height:1.3}
  .side-ingredients{font-family:"Oswald",sans-serif;font-weight:300;font-size:16px;margin-top:2px;line-height:1.3}
  .side-perks{font-family:"Oswald",sans-serif;font-weight:400;font-size:14.5px;line-height:1.45;margin-top:14px}
  .badges{display:flex;justify-content:center;gap:14px;margin-top:24px}
  .badge{width:54px;height:54px;border-radius:50%;border:3px solid rgba(255,255,255,.9)}
  .band-amber--side{font-size:21px;text-transform:uppercase}

  .side-copy{padding:30px 28px 0;font-family:"Oswald",sans-serif;font-weight:300;font-size:14px;line-height:1.55;color:var(--ink)}
  .side-copy p+p{margin-top:14px}
  .side-copy strong{font-weight:500}
  .side-maker{margin-top:22px;font-weight:400}
  .side-fields{font-weight:400;text-align:left;display:inline-block}
</style>
</head>
<body>
<main class="stage">
  <div class="box">

    <section class="panel panel--side">
      <header class="brand">
        <span class="brand__dot"></span>
        <span class="brand__name">Velmora</span>
      </header>
      <div class="band-green side-green">
        <h2 class="side-heading">Declaration of Ingredients</h2>
        <p class="side-ingredients">fractionated coconut oil, CBD hemp extract</p>
        <p class="side-perks">Contains omega 3, 6 and essential fatty acids<br>Graduated dropper for precise dosing<br>40mg of CBD per dropper!</p>
        <div class="badges">
          <span class="badge" role="img" aria-label="Certified clean hemp badge"></span>
          <span class="badge" role="img" aria-label="GMP certified badge"></span>
          <span class="badge" role="img" aria-label="Made in USA badge"></span>
        </div>
      </div>
      <div class="band-amber band-amber--side">1200MG CBD Tincture</div>
      <div class="lower">
        <div class="lower__wash" role="img" aria-label="Soft pattern of faint drops"></div>
        <div class="lower__content side-copy">
          <p>These statements have not been evaluated by the Food and Drug Administration. FDA has not evaluated this product for safety or efficacy. This product is not intended to diagnose, treat, cure or prevent any disease.</p>
          <p>DO NOT REFRIGERATE. Keep at room temperature to preserve freshness. Store away from humidity, heat, and light.</p>
          <p><strong>Warning:</strong> If pregnant, nursing or taking prescription drugs, consult your physician prior to use. Keep out of reach of children.</p>
          <p class="side-maker">Manufactured by<br>Velmora CBD Co. 58 Quarry Bend Rd.<br>Scarborough, ME 04019</p>
          <p class="side-fields">Batch ID: ____________________<br>Expiration Date: ______________</p>
        </div>
      </div>
    </section>

    <section class="panel panel--front">
      <header class="brand">
        <span class="brand__dot"></span>
        <span class="brand__name">Velmora</span>
      </header>
      <div class="band-green">
        <p class="front-spectrum">FULL SPECTRUM SUPERCRITICAL CO2</p>
        <h1 class="front-title">HEMP<br>EXTRACT</h1>
      </div>
      <div class="band-amber band-amber--front">Made from TRUNK certified clean hemp</div>
      <div class="lower">
        <div class="lower__wash" role="img" aria-label="Soft pattern of faint drops"></div>
        <div class="lower__content">
          <div class="front-mark"></div>
          <p class="front-mg">1200MG</p>
          <p class="front-cbd">CBD</p>
          <p class="front-tincture">TINCTURE</p>
          <p class="front-net">NT. WT. 1FL OZ (30ML)</p>
        </div>
      </div>
    </section>

  </div>
</main>
</body>
</html>
```